Building company buisness cards

We are looking for a sharp modern new look for our business cards.
We are a New Zealand based company that specialises in house and land packages.
We have attached a photo of the current logo and would like to see if it can be improved somehow if needed.
We are open to any colours but we have chosen green at this stage.
Feel free to change the font and make the logo smarter looking.
Play with the colours and see what looks best.

We want a card that looks so good know one will want to throw it away!

Target Market(s)

Home buyers

Industry/Entity Type

Building

Contact Information for Business Card

Dorian Keswick
0217392604
dkeswick@tidewellhomecraft.co.nz
tidewellhomecraft.co.nz

Font styles to use
Serif
Sans Serif

Colors

Designer to choose colors to be used in the design.

Requirements
Must have
• Logo and company name on one side, details on the other side
Nice to have
• Color codes for the original green are HEX #4a8028, RGB(74,128,40), CMYK(42,0,69,50)
• Round corners, Raised and/or spot UV

```html
<!DOCTYPE html>
<html lang="en">
<head>
<meta charset="utf-8">
<title>Tidewell Homecraft — Business Cards</title>
<link rel="stylesheet" href="https://fonts.googleapis.com/css2?family=Open+Sans:wght@300;400;700&display=swap">
<style>
  :root {
    --brand-green: #1e8c1e;
    --ink: #1a1a1a;
    --muted-ink: #444444;
    --rule: #d6d6d6;
    --card: #ffffff;
    --backdrop: #2b2b2b;
  }
  * { margin: 0; padding: 0; box-sizing: border-box; }
  html, body {
    width: 1200px;
    height: 716px;
    overflow: hidden;
    background: var(--backdrop);
    font-family: "Open Sans", Arial, sans-serif;
  }
  .sheet {
    width: 1200px;
    height: 716px;
    display: flex;
    align-items: center;
    justify-content: center;
    gap: 60px;
  }
  .card {
    width: 500px;
    height: 286px;
    background: var(--card);
    border-radius: 6px;
    box-shadow: 0 10px 24px rgba(0, 0, 0, 0.45);
    display: flex;
    flex-direction: column;
    align-items: center;
    justify-content: center;
  }
  .wordmark {
    display: flex;
    align-items: center;
    gap: 12px;
    color: var(--brand-green);
    font-weight: 400;
    text-transform: uppercase;
    letter-spacing: 3px;
    line-height: 1;
    white-space: nowrap;
  }
  .wordmark__mark {
    width: 12px;
    height: 12px;
    background: var(--brand-green);
    flex: none;
  }
  .card--front .wordmark { font-size: 18px; }
  .card--back .wordmark { font-size: 26px; gap: 16px; }
  .card--back .wordmark__mark { width: 16px; height: 16px; }
  .divider {
    width: 44px;
    height: 1px;
    background: var(--rule);
    margin: 14px 0 12px;
  }
  .card--back .divider { width: 60px; margin-top: 18px; }
  .details {
    display: flex;
    flex-direction: column;
    align-items: flex-start;
    gap: 5px;
  }
  .details__name {
    color: var(--brand-green);
    font-weight: 300;
    font-size: 21px;
    margin-bottom: 2px;
  }
  .details__phone {
    color: var(--ink);
    font-weight: 700;
    font-size: 12px;
    letter-spacing: 0.5px;
  }
  .details__email,
  .details__web {
    color: var(--muted-ink);
    font-weight: 400;
    font-size: 11px;
  }
</style>
</head>
<body>
  <main class="sheet">
    <section class="card card--front" aria-label="Business card, details side">
      <div class="wordmark">
        <span class="wordmark__mark"></span>
        <span class="wordmark__name">Tidewell Homecraft</span>
      </div>
      <div class="divider"></div>
      <div class="details">
        <p class="details__name">Dorian Keswick</p>
        <p class="details__phone">0217392604</p>
        <p class="details__email">dkeswick@tidewellhomecraft.co.nz</p>
        <p class="details__web">tidewellhomecraft.co.nz</p>
      </div>
    </section>

    <section class="card card--back" aria-label="Business card, name side">
      <div class="wordmark">
        <span class="wordmark__mark"></span>
        <span class="wordmark__name">Tidewell Homecraft</span>
      </div>
      <div class="divider"></div>
    </section>
  </main>
</body>
</html>
```